The Lantern Den Business Cards

We are a Craft Beer/Upscale dining Bar/Restaurant. We'll have 24 taps of craft beers and several types of bottled beers. In addition, we'll be serving a variety of top shelf bourbons, spirits and wines with a small unique menu. I'd like the design to be sophisticated, elegant and modern while staying away from "cartoonish" pictures.
Updates
Hello, I've added some example logos for inspiration. I'd like to use a lot of black/white with maybe a little color for a "pop". Thank you!
Industry/Entity Type
Business
Contact Information for Business Card
THE LANTERN DEN
Tomas Orlikova
582 Wexmoor Street
Norfolk, Virginia 23847
Office: (757) 555-0143
Mobile: (757) 555-0178
Look and feel
Each slider illustrates characteristics of the customer's brand and the style your logo design should communicate.

```html
<!DOCTYPE html>
<html lang="en">
<head>
<meta charset="utf-8">
<title>The Lantern Den — Business Card</title>
<link rel="stylesheet" href="https://fonts.googleapis.com/css2?family=Josefin+Sans:wght@300;400&display=swap">
<style>
  :root {
    --paper: #ffffff;
    --card: #000000;
    --ink: #ffffff;
    --seal: #262626;
    --rule: #8a8a8a;
  }
  * { margin: 0; padding: 0; box-sizing: border-box; }
  html, body {
    width: 1200px;
    height: 693px;
    overflow: hidden;
    background: var(--paper);
  }
  .card {
    position: absolute;
    left: 11px;
    top: 14px;
    width: 1178px;
    height: 667px;
    background: var(--card);
    color: var(--ink);
    font-family: "Josefin Sans", sans-serif;
    font-weight: 300;
  }
  .emblem {
    position: absolute;
    left: 0;
    top: 0;
    width: 1178px;
    height: 667px;
  }
  .business-name {
    font-family: "Josefin Sans", sans-serif;
    font-weight: 300;
    font-size: 48px;
    letter-spacing: 6px;
    fill: var(--ink);
  }
  .address-arc {
    font-family: "Josefin Sans", sans-serif;
    font-weight: 300;
    font-size: 19px;
    letter-spacing: 1.5px;
    fill: var(--ink);
  }
  .person-name {
    position: absolute;
    left: 0;
    width: 100%;
    top: 551px;
    text-align: center;
    font-size: 27px;
    letter-spacing: 2.5px;
  }
  .contact-row {
    position: absolute;
    left: 0;
    width: 100%;
    top: 601px;
    display: flex;
    justify-content: center;
    align-items: center;
    font-size: 24px;
    letter-spacing: 1px;
  }
  .contact {
    display: flex;
    align-items: center;
    gap: 8px;
  }
  .contact svg { fill: var(--ink); }
  .divider {
    width: 1px;
    height: 38px;
    background: var(--rule);
    margin: 0 38px;
  }
</style>
</head>
<body>
  <main class="card">
    <svg class="emblem" viewBox="0 0 1178 667" aria-hidden="false">
      <defs>
        <path id="address-path" d="M 417 342 A 170 170 0 0 0 757 342"/>
      </defs>
      <text class="business-name" x="587" y="195" text-anchor="middle">THE LANTERN DEN</text>
      <circle class="seal" cx="587" cy="342" r="112" fill="var(--seal)"/>
      <text class="address-arc">
        <textPath href="#address-path" startOffset="50%" text-anchor="middle">582 WEXMOOR STREET NORFOLK, VIRGINIA 23847</textPath>
      </text>
    </svg>

    <p class="person-name">TOMAS ORLIKOVA</p>

    <div class="contact-row">
      <span class="contact office">
        <svg width="28" height="20" viewBox="0 0 28 20" aria-label="Office phone" role="img">
          <path d="M1 7 C1 2 27 2 27 7 L27 9 L20 9 L20 6 C16 5 12 5 8 6 L8 9 L1 9 Z"/>
          <path d="M7 10 L21 10 L25 19 L3 19 Z"/>
          <circle cx="14" cy="14" r="3" fill="var(--card)"/>
        </svg>
        (757) 555-0143
      </span>
      <span class="divider"></span>
      <span class="contact mobile">
        <svg width="18" height="30" viewBox="0 0 18 30" aria-label="Mobile phone" role="img">
          <rect x="1" y="1" width="16" height="28" rx="3"/>
          <rect x="4" y="5" width="10" height="16" fill="var(--card)"/>
          <circle cx="9" cy="25" r="1.6" fill="var(--card)"/>
        </svg>
        (757) 555-0178
      </span>
    </div>
  </main>
</body>
</html>
```